Forest Consultant/Timber Buyer needs a clean business card

We are a forestry consulting and timber buying company. We meet with private landowners and assist them with timber management and timber harvesting. We would like a professional business card, please no clip art. logo is blue and white but would like to see a gray,silver, or some other color incorporated. Would like basic contact info. Would like to the layout to be creative and sleek but masculine.

Target Market(s)

private landowners

Industry/Entity Type

Business

Contact Information for Business Card

name,position, cell number, office number, email, website. This might be to cluttered. Basic contact info is what we are looking for.

Contact info can all be on one side with logo on the other.

Font styles to use
Serif
Sans Serif

Colors
0255a3
ffffff
aaaaaa

Requirements
Must have
• We just want it professional.
Nice to have
• Creative layout.
Should not have
• please no clip art of log trucks etc.

```html
<!DOCTYPE html>
<html lang="en">
<head>
<meta charset="utf-8">
<title>Cedarline Forestry – Business Card</title>
<link rel="stylesheet" href="https://fonts.googleapis.com/css2?family=Arimo:wght@400;700&display=swap">
<style>
  :root {
    --brand-blue: #0253a1;
    --brand-blue-deep: #0a3a73;
    --band-gray: #7f94ad;
    --band-gray-edge: #5d7390;
    --band-shadow: #01305f;
    --ink-white: #ffffff;
    --mark-blue: #0a3f7c;
  }
  * { margin: 0; padding: 0; box-sizing: border-box; }
  html, body {
    width: 1200px; height: 706px; overflow: hidden;
    background: var(--brand-blue);
  }
  .card {
    position: relative;
    width: 1200px; height: 706px;
    background: var(--brand-blue);
    font-family: "Arimo", Arial, sans-serif;
    color: var(--ink-white);
    overflow: hidden;
  }
  .identity {
    position: absolute;
    right: 785px; top: 170px;
    text-align: right;
    white-space: nowrap;
  }
  .identity__name {
    font-weight: 700;
    font-size: 40px;
    letter-spacing: 1px;
    line-height: 46px;
    text-align: left;
    padding-bottom: 4px;
    border-bottom: 2px solid var(--ink-white);
  }
  .identity__role {
    font-weight: 400;
    font-size: 36px;
    line-height: 50px;
  }
  .bands {
    position: absolute; left: 0; top: 0;
    width: 1200px; height: 706px;
  }
  .contact {
    position: absolute;
    font-size: 23px;
    line-height: 38px;
    white-space: pre;
  }
  .contact--phone { left: 111px; top: 453px; }
  .contact--web { left: 106px; top: 589px; }
  .brand-mark {
    position: absolute;
    left: 914px; top: 300px;
    transform: translate(-50%, -50%);
    display: flex;
    align-items: center;
    gap: 18px;
    white-space: nowrap;
  }
  .brand-mark__dot {
    display: block;
    width: 56px; height: 56px;
    border-radius: 50%;
    background: var(--mark-blue);
  }
  .brand-mark__name {
    font-weight: 700;
    font-size: 42px;
    line-height: 50px;
    color: var(--mark-blue);
  }
</style>
</head>
<body>
<main class="card">
  <svg class="bands" viewBox="0 0 1200 706" aria-hidden="true">
    <polygon points="0,428 588,428 652,546 0,546" fill="var(--band-shadow)"/>
    <polygon points="0,431 584,431 644,541 0,541" fill="var(--band-gray)"/>
    <polygon points="0,443 576,443 628,533 0,533" fill="none" stroke="var(--band-gray-edge)" stroke-width="2"/>
    <polygon points="0,570 652,570 588,690 0,690" fill="var(--band-shadow)"/>
    <polygon points="0,575 642,575 584,684 0,684" fill="var(--brand-blue)"/>
    <polygon points="0,581 630,581 578,677 0,677" fill="none" stroke="var(--band-shadow)" stroke-width="2"/>
    <g class="icon-phone">
      <rect x="48" y="466" width="27" height="54" rx="4" fill="var(--ink-white)"/>
      <rect x="51" y="471" width="21" height="24" fill="var(--brand-blue-deep)"/>
      <g fill="var(--brand-blue-deep)">
        <rect x="52" y="499" width="4" height="3"/><rect x="59" y="499" width="4" height="3"/><rect x="66" y="499" width="4" height="3"/>
        <rect x="52" y="505" width="4" height="3"/><rect x="59" y="505" width="4" height="3"/><rect x="66" y="505" width="4" height="3"/>
        <rect x="52" y="511" width="4" height="3"/><rect x="59" y="511" width="4" height="3"/><rect x="66" y="511" width="4" height="3"/>
      </g>
    </g>
    <g class="icon-mouse" fill="none" stroke="var(--ink-white)" stroke-width="2.5">
      <path d="M20,622 C30,620 38,612 42,600 C44,594 48,594 52,600"/>
      <rect x="44" y="604" width="33" height="48" rx="16" fill="var(--ink-white)"/>
      <line x1="60" y1="606" x2="60" y2="624" stroke="var(--brand-blue)"/>
      <line x1="45" y1="624" x2="76" y2="624" stroke="var(--brand-blue)"/>
    </g>
  </svg>

  <section class="identity">
    <h1 class="identity__name">DALE CARTER</h1>
    <p class="identity__role">Manager</p>
  </section>

  <p class="contact contact--phone">Phone   :   + 000 - 0000 - 0000
Office    :   + 000 - 0000 - 0000</p>

  <p class="contact contact--web">E-Mail    : admin@CedarlineForestry.com
Website : www.CedarlineForestry.com</p>

  <div class="brand-mark">
    <span class="brand-mark__dot"></span>
    <p class="brand-mark__name">Cedarline Forestry</p>
  </div>
</main>
</body>
</html>
```